Business Card design, kestrel shipping

I started a container shipping company which specialized in export of cars, motorcycles, boats and general cargo overseas. I need a business card that stands out of the pack and gives clients an idea of what I do. I have attached a sample that someone designed for me but I don't think its the right fit. However the info on it is accurate so can be used right on new card.

Reason: I would like my new logo which is being designed on VORMLYNTA.COM as well to be implemented into my business card.

Industry/Entity Type

Shipping

```html
<!DOCTYPE html>
<html lang="en">
<head>
<meta charset="utf-8">
<title>Kestrel Shipping — Business Card</title>
<link rel="stylesheet" href="https://fonts.googleapis.com/css2?family=Lato:wght@400;700&display=swap">
<style>
  :root {
    --brand-blue: #1638ee;
    --brand-blue-light: #5b8cf5;
    --card-white: #ffffff;
    --card-grey: #eeeeef;
    --page-bg: #e4e6ea;
    --text-white: #ffffff;
  }
  * { box-sizing: border-box; margin: 0; padding: 0; }
  html, body {
    width: 1200px; height: 900px; overflow: hidden;
    background: var(--page-bg);
  }
  .canvas {
    width: 1200px; height: 900px;
    display: flex; flex-direction: column; align-items: center; justify-content: center;
    gap: 60px;
  }
  .card {
    width: 595px; height: 340px;
    position: relative; overflow: hidden;
    box-shadow: 0 10px 28px rgba(0,0,0,0.18);
  }

  /* Shared wordmark */
  .wordmark {
    display: flex; align-items: center; gap: 14px;
    font-family: "Lato", sans-serif; font-weight: 700;
  }
  .wordmark-dot { border-radius: 50%; flex: none; }

  /* Front */
  .card-front {
    background: var(--brand-blue);
    display: flex; align-items: center; justify-content: center;
    color: var(--text-white);
  }
  .card-front .wordmark { font-size: 44px; }
  .card-front .wordmark-dot { width: 20px; height: 20px; background: var(--text-white); }

  /* Back */
  .card-back {
    background: linear-gradient(180deg, var(--card-white) 0%, var(--card-grey) 100%);
  }
  .back-mark {
    position: absolute; top: 0; left: 0; right: 0; height: 158px;
    display: flex; align-items: center; justify-content: center;
  }
  .back-mark .wordmark { font-size: 30px; gap: 12px; color: var(--brand-blue); }
  .back-mark .wordmark-dot { width: 16px; height: 16px; background: var(--brand-blue); }

  .contact-band {
    position: absolute; left: 0; right: 0; top: 158px; height: 150px;
    background: var(--brand-blue); color: var(--text-white);
    font-family: "Lato", sans-serif;
  }
  .person {
    position: absolute; left: 118px; top: 28px; width: 200px; text-align: center;
  }
  .person-name { font-size: 25px; font-weight: 400; line-height: 30px; }
  .person-role { font-size: 17px; color: var(--brand-blue-light); line-height: 22px; }
  .address {
    position: absolute; left: 118px; top: 96px;
    font-size: 15px; line-height: 21px;
  }
  .contact-list {
    position: absolute; left: 350px; top: 14px; list-style: none;
    font-size: 17px;
  }
  .contact-list li { display: flex; align-items: center; gap: 9px; height: 25px; }
  .contact-icon {
    width: 16px; height: 16px; background: var(--text-white); border-radius: 2px;
    display: flex; align-items: center; justify-content: center;
  }
  .bottom-strip {
    position: absolute; left: 0; right: 0; bottom: 0; height: 32px;
    background: var(--card-white);
  }
</style>
</head>
<body>
<main class="canvas">
  <section class="card card-front" aria-label="Card front">
    <div class="wordmark">
      <span class="wordmark-dot"></span>
      <span class="wordmark-name">Kestrel Shipping</span>
    </div>
  </section>

  <section class="card card-back" aria-label="Card back">
    <div class="back-mark">
      <div class="wordmark">
        <span class="wordmark-dot"></span>
        <span class="wordmark-name">Kestrel Shipping</span>
      </div>
    </div>
    <div class="contact-band">
      <div class="person">
        <p class="person-name">Mara Ellison</p>
        <p class="person-role">Managing Director</p>
      </div>
      <p class="address">12 Address Goes Here<br>1234 City, Country 12345</p>
      <ul class="contact-list">
        <li><span class="contact-icon"><svg width="10" height="10" viewBox="0 0 10 10"><path d="M2 1 L4 1 L4.6 3 L3.4 3.8 Q4.4 5.8 6.2 6.6 L7 5.4 L9 6 L9 8 Q5 9 1 5 Q1 3 2 1Z" fill="#1638ee"/></svg></span>555-014-2260</li>
        <li><span class="contact-icon"><svg width="10" height="10" viewBox="0 0 10 10"><path d="M2 1 L4 1 L4.6 3 L3.4 3.8 Q4.4 5.8 6.2 6.6 L7 5.4 L9 6 L9 8 Q5 9 1 5 Q1 3 2 1Z" fill="#1638ee"/></svg></span>555-014-2261</li>
        <li><span class="contact-icon"><svg width="11" height="9" viewBox="0 0 11 9"><rect x="0.5" y="0.5" width="10" height="8" fill="none" stroke="#1638ee"/><path d="M0.5 0.5 L5.5 5 L10.5 0.5" fill="none" stroke="#1638ee"/></svg></span>info@kestrelship.com</li>
        <li><span class="contact-icon"><svg width="10" height="10" viewBox="0 0 10 10"><circle cx="5" cy="5" r="4" fill="none" stroke="#1638ee"/><path d="M1 5 H9 M5 1 Q2.5 5 5 9 M5 1 Q7.5 5 5 9" fill="none" stroke="#1638ee" stroke-width="0.8"/></svg></span>www.kestrelship.com</li>
      </ul>
    </div>
    <div class="bottom-strip"></div>
  </section>
</main>
</body>
</html>
```